Menu Design Project

Bo velle hair and beauty service menu
we need a menu to display a handful of our services to give our customers an idea of our pricing

Cutting
Ladies cuts from $35
Men's cuts from $25
All cuts are included with a wash and dry off

Quorvel colours
All over colours start from $55
price will vary depending upon length and thickness of hair

Foiling
starts from $50
Price will vary depending upon length of hair

Toners
from $30

Blowdries
from $35

Upstyling
wedding styling from $45
Please enquire for special occasion styling also

Beauty Services

Waxing
Eyebrow wax and shape $17.50
Lip $10
Chin/sides $20
Legs from $25
Bikini $20
XX $30
XXX $45
Back from $25
Chest from $25

Eyes
Eyebrow tinting $15
Eyelash tinting $20
Eyelash extensions from $90

Sandrift facials
Express facial $45
Deluxe facial $95

Acrylic nails
full set $60
Gel polish $35
Manicures from $35
Pedicures from $45

can provide logo and other images to help

Industry/Entity Type

Hair

Requirements
Must have
• must be called a service menu
must be eye catching and memorable but not excessive
Nice to have
• postcard style size hair menu on one side
beauty menu on the other side
elegant classy design
Should not have
• must not be called a price list
stay away from traditional price list style in terms of folding out leaflet

```html
<!DOCTYPE html>
<html lang="en">
<head>
<meta charset="UTF-8">
<title>Beauty Services Menu</title>
<link rel="stylesheet" href="https://fonts.googleapis.com/css2?family=Inter:wght@200;300;400&display=swap">
<style>
  :root {
    --paper: #f4f6f9;
    --paper-cool: #e9edf2;
    --skin-light: #efe3de;
    --skin-mid: #dcc3b8;
    --skin-warm: #c9a597;
    --hair-dark: #3a2f2c;
    --ink-heading: #1f1f1f;
    --ink-item: #4a4a4a;
    --ink-title: #3d3d3d;
  }
  * { margin: 0; padding: 0; box-sizing: border-box; }
  html, body { width: 1200px; height: 866px; overflow: hidden; }
  body {
    position: relative;
    background: linear-gradient(90deg, var(--paper) 0%, var(--paper-cool) 100%);
    font-family: "Inter", "Helvetica Neue", Arial, sans-serif;
  }
  .portrait-area {
    position: absolute;
    top: 0; right: 0;
    width: 720px; height: 866px;
    background:
      radial-gradient(ellipse 260px 200px at 640px 90px, var(--hair-dark) 0%, rgba(58,47,44,0.5) 55%, rgba(58,47,44,0) 100%),
      radial-gradient(ellipse 380px 460px at 470px 470px, var(--skin-mid) 0%, var(--skin-light) 55%, rgba(239,227,222,0) 100%),
      linear-gradient(90deg, rgba(244,246,249,0) 0%, var(--skin-light) 35%, var(--skin-warm) 100%);
  }
  .section-title {
    position: absolute;
    left: 86px;
    top: 786px;
    transform-origin: 0 0;
    transform: rotate(-90deg);
    font-size: 53px;
    font-weight: 200;
    color: var(--ink-title);
    letter-spacing: -0.5px;
    white-space: nowrap;
    line-height: 1;
  }
  .service-group {
    position: absolute;
    left: 165px;
    width: 380px;
  }
  .group-heading {
    font-size: 22px;
    font-weight: 400;
    letter-spacing: 0.5px;
    color: var(--ink-heading);
    line-height: 28px;
  }
  .service-list { list-style: none; }
  .service-item {
    display: flex;
    align-items: baseline;
    height: 28px;
    line-height: 28px;
    white-space: nowrap;
  }
  .service-name {
    width: 297px;
    font-size: 23.5px;
    font-weight: 200;
    color: var(--ink-item);
    letter-spacing: 0;
  }
  .service-price {
    font-size: 14px;
    font-weight: 300;
    letter-spacing: 0.6px;
    color: var(--ink-heading);
  }
  .group-waxing { top: 85px; }
  .group-eyes { top: 394px; }
  .group-facials { top: 534px; }
  .group-nails { top: 647px; }
</style>
</head>
<body>
  <div class="portrait-area" role="img" aria-label="Soft-focus photograph of a relaxed woman with closed eyes resting her head on her hand"></div>

  <h1 class="section-title">Beauty Services</h1>

  <section class="service-group group-waxing">
    <h2 class="group-heading">Waxing</h2>
    <ul class="service-list">
      <li class="service-item"><span class="service-name">Eyebrow wax and shape</span><span class="service-price">$17.50</span></li>
      <li class="service-item"><span class="service-name">Lip</span><span class="service-price">$10</span></li>
      <li class="service-item"><span class="service-name">Chin/sides</span><span class="service-price">$20</span></li>
      <li class="service-item"><span class="service-name">Legs from</span><span class="service-price">$25</span></li>
      <li class="service-item"><span class="service-name">Bikini</span><span class="service-price">$20</span></li>
      <li class="service-item"><span class="service-name">XX</span><span class="service-price">$30</span></li>
      <li class="service-item"><span class="service-name">XXX</span><span class="service-price">$45</span></li>
      <li class="service-item"><span class="service-name">Back from</span><span class="service-price">$25</span></li>
      <li class="service-item"><span class="service-name">Chest from</span><span class="service-price">$25</span></li>
    </ul>
  </section>

  <section class="service-group group-eyes">
    <h2 class="group-heading">Eyes</h2>
    <ul class="service-list">
      <li class="service-item"><span class="service-name">Eyebrow tinting</span><span class="service-price">$15</span></li>
      <li class="service-item"><span class="service-name">Eyelash tinting</span><span class="service-price">$20</span></li>
      <li class="service-item"><span class="service-name">Eyelash extensions from</span><span class="service-price">$90</span></li>
    </ul>
  </section>

  <section class="service-group group-facials">
    <h2 class="group-heading">Sandrift facials</h2>
    <ul class="service-list">
      <li class="service-item"><span class="service-name">Express facial</span><span class="service-price">$45</span></li>
      <li class="service-item"><span class="service-name">Deluxe facial</span><span class="service-price">$95</span></li>
    </ul>
  </section>

  <section class="service-group group-nails">
    <h2 class="group-heading">Acrylic nails</h2>
    <ul class="service-list">
      <li class="service-item"><span class="service-name">full set</span><span class="service-price">$60</span></li>
      <li class="service-item"><span class="service-name">Gel polish</span><span class="service-price">$35</span></li>
      <li class="service-item"><span class="service-name">Manicures from</span><span class="service-price">$35</span></li>
      <li class="service-item"><span class="service-name">Pedicures from</span><span class="service-price">$45</span></li>
    </ul>
  </section>
</body>
</html>
```